Need DL Flyer for Real Estate Drops

We need a real estate flyer ,double sided. With content on 1 side like: Want to know what's your house is worth " contact us today and on other side agent details. We are looking for an ongoing partnership with designer so this assignment will be ongoing

```html
<!DOCTYPE html>
<html lang="en">
<head>
<meta charset="utf-8">
<title>DL Flyer – Meridian Real Estate</title>
<link rel="stylesheet" href="https://fonts.googleapis.com/css2?family=Montserrat:wght@300;400;500;700;800;900&display=swap">
<style>
  :root {
    --backdrop: #a7a7a7;
    --paper: #ffffff;
    --brand-red: #c8202a;
    --deep-red: #b51d25;
    --navy: #1b1f3b;
    --slate: #3f4248;
    --mid-grey: #6b6e75;
    --soft-grey: #a4a6ab;
    --photo-light: #f1f1f3;
    --photo-mid: #c9ccd2;
    --portrait-blue: #9aaccc;
  }
  * { box-sizing: border-box; margin: 0; padding: 0; }
  html, body {
    width: 1200px; height: 727px; overflow: hidden;
    background: var(--backdrop);
    font-family: "Montserrat", Arial, sans-serif;
  }
  .flyer-spread {
    position: relative; width: 1200px; height: 727px;
    display: flex; justify-content: center; align-items: center; gap: 60px;
  }
  .flyer-side {
    position: relative; width: 310px; height: 651px;
    background: var(--paper);
    display: flex; flex-direction: column; align-items: center;
    overflow: hidden;
  }

  /* brand lockup */
  .brand {
    position: relative;
    display: flex; align-items: center; gap: 10px;
    color: var(--navy); font-weight: 700; font-size: 19px; letter-spacing: 0.2px;
    white-space: nowrap;
  }
  .brand-mark { width: 26px; height: 26px; background: var(--brand-red); flex: none; }

  /* front side */
  .front { padding-top: 34px; }
  .headline { position: relative; margin-top: 26px; text-align: center; line-height: 1; }
  .headline-lead {
    display: block; font-weight: 300; font-size: 17px; letter-spacing: 9px;
    color: var(--soft-grey); padding-left: 9px;
  }
  .headline-mid {
    display: block; margin-top: 6px; font-weight: 900; font-size: 40px;
    letter-spacing: -1.5px; color: var(--slate);
  }
  .headline-big {
    display: block; margin-top: -2px; font-weight: 900; font-size: 68px;
    letter-spacing: -2px; color: var(--deep-red);
  }
  .hero-photo {
    position: absolute; left: 0; right: 0; top: 235px; bottom: 0;
    background: linear-gradient(180deg, var(--paper) 0%, var(--photo-light) 25%, var(--photo-mid) 100%);
  }
  .cta {
    position: absolute; bottom: 34px; left: 50%; transform: translateX(-50%);
    padding: 9px 22px; border: 2px solid var(--brand-red); border-radius: 30px;
    background: var(--paper); white-space: nowrap;
    color: var(--brand-red); font-size: 15px; letter-spacing: 0.3px;
  }
  .cta strong { font-weight: 800; }
  .cta span { font-weight: 500; }

  /* back side */
  .back { padding-top: 46px; }
  .agent-photo {
    width: 168px; height: 168px; border-radius: 50%;
    background: linear-gradient(135deg, var(--brand-red) 0%, var(--brand-red) 45%, var(--portrait-blue) 100%);
  }
  .agent-name {
    margin-top: 30px; font-weight: 800; font-size: 24px; color: var(--navy);
  }
  .name-rule { width: 46px; height: 1px; background: var(--soft-grey); margin-top: 10px; }
  .phone-list { margin-top: 28px; list-style: none; }
  .phone-list li {
    display: flex; align-items: center; gap: 10px;
    font-size: 17px; color: var(--mid-grey); letter-spacing: 0.5px; line-height: 1.6;
  }
  .phone-list svg { width: 16px; height: 16px; flex: none; }
  .web-list { margin-top: 22px; list-style: none; text-align: center; }
  .web-list li {
    font-size: 11.5px; color: var(--mid-grey); letter-spacing: 0.3px; line-height: 1.9;
  }
  .web-list .site { border-top: 1px solid var(--soft-grey); }
  .web-list b { font-weight: 700; color: var(--slate); }
  .back .brand { margin-top: auto; margin-bottom: 70px; font-size: 21px; }
</style>
</head>
<body>
<main class="flyer-spread">

  <section class="flyer-side front" aria-label="Flyer front">
    <div class="hero-photo" role="img" aria-label="Photo of a hand holding a small grey model house"></div>
    <div class="brand"><i class="brand-mark"></i>Meridian Real Estate</div>
    <h1 class="headline">
      <span class="headline-lead">WANT TO KNOW</span>
      <span class="headline-mid">YOUR HOUSE</span>
      <span class="headline-big">WORTH</span>
    </h1>
    <p class="cta"><strong>CONTACT US</strong> <span>TODAY</span></p>
  </section>

  <section class="flyer-side back" aria-label="Flyer back">
    <div class="agent-photo" role="img" aria-label="Portrait of the agent in a light blue suit on a red circle"></div>
    <h2 class="agent-name">Rohan Mehta</h2>
    <div class="name-rule"></div>
    <ul class="phone-list">
      <li>
        <svg viewBox="0 0 16 16" aria-hidden="true"><rect x="4" y="1" width="8" height="5" fill="none" stroke="var(--brand-red)" stroke-width="1.5"/><rect x="1" y="5" width="14" height="10" rx="2" fill="var(--brand-red)"/><rect x="4" y="8" width="8" height="4" fill="#fff"/></svg>
        (03) 5550 1234
      </li>
      <li>
        <svg viewBox="0 0 16 16" aria-hidden="true"><rect x="0" y="0" width="16" height="16" rx="3" fill="var(--brand-red)"/><path d="M4.5 3.5l2 2-1 1.3c.7 1.5 1.8 2.6 3.2 3.2l1.3-1 2 2-1.2 1.5C7.5 12.2 3.8 8.5 3.5 4.7z" fill="#fff"/></svg>
        0400555019
      </li>
    </ul>
    <ul class="web-list">
      <li>rohan@meridianrealestate.com.au</li>
      <li class="site">www.<b>meridianrealestate</b>.com.au</li>
    </ul>
    <div class="brand"><i class="brand-mark"></i>Meridian Real Estate</div>
  </section>

</main>
</body>
</html>
```